Flyer for American Indian Elders on Dementia Warning Signs

We need a flyer designed for older adults who are American Indian or Alaska Native (in the U.S.).

Ideally, the flyer should complement the colors of our logos. The project logo and our organization logo are attached to the brief.

When people see the flyer we want them to feel that it represents their culture, is warm, and professional but relatable to older adults and people who have limited incomes.

I have attached an earlier draft of the document we designed ourselves BUT we want different and better.

It is for older adults who have trouble reading so:
1. you must use a font that is 11.5 points or larger
2. Do not put text over complex pictures or use shading with words
3. You can use a serif font for the heading, but should use san serif for the body text
4. There should be good contrast between the font color and background

Please do not use any images that include a head dress or pictures of American Indian people or things that are very traditional or "token" imagery.

We need to save a small space under the call out box/ somewhere on the flyer for other people to add their logo once they download.

Let us know if you have questions or need additional information.

Target Market(s)

Older American Indian people

Font styles to use
Serif
Sans Serif

Requirements
Must have
• Easy to read for older adults
Should not have
• indian headdress

```html
<!DOCTYPE html>
<html lang="en">
<head>
<meta charset="utf-8">
<title>10 Warning Signs of Abnormal Memory Changes or Dementia</title>
<link href="https://fonts.googleapis.com/css2?family=Carlito:wght@400;700&family=Jost:wght@600;700&display=swap" rel="stylesheet">
<style>
  :root {
    --page-bg: #ece7e2;
    --paper: #ffffff;
    --rose: #e8877e;
    --rose-light: #f1b9ad;
    --rose-deep: #e9756a;
    --title-ink: #4a3034;
    --ink: #1f1a1a;
    --teal: #0e7791;
    --teal-dark: #0b6278;
    --link-red: #b5342d;
    --marker-red: #c9463d;
    --callout-ink: #4a2e30;
  }
  * { box-sizing: border-box; margin: 0; padding: 0; }
  html, body { width: 1200px; height: 760px; overflow: hidden; }
  body { background: var(--page-bg); font-family: "Carlito", "Calibri", sans-serif; color: var(--ink); }

  .flyer {
    position: absolute; left: 315px; top: 12px;
    width: 570px; height: 736px;
    background: var(--paper);
    box-shadow: 0 4px 18px rgba(0,0,0,.18);
    overflow: hidden;
  }

  /* Left column */
  .title-band {
    position: absolute; left: 0; top: 0; width: 339px; height: 80px;
    background: var(--rose);
    border-bottom: 7px solid var(--rose-light);
    text-align: center; color: var(--title-ink);
    font-family: "Jost", "Futura", sans-serif; font-weight: 700;
    padding-top: 6px;
  }
  .title-main { font-size: 30px; line-height: 32px; letter-spacing: .3px; }
  .title-sub { font-size: 15.5px; line-height: 19px; letter-spacing: .3px; }

  .intro {
    position: absolute; left: 14px; top: 97px; width: 311px;
    font-size: 10.3px; line-height: 13.4px;
  }
  .intro strong { font-weight: 700; }

  .signs {
    position: absolute; left: 14px; top: 200px; width: 311px; height: 486px;
    list-style: none;
    display: flex; flex-direction: column; justify-content: space-between;
  }
  .sign {
    display: grid; grid-template-columns: 23px 1fr; column-gap: 10px; align-items: center;
    font-size: 10.3px; line-height: 13.4px;
  }
  .sign-num {
    width: 23px; height: 23px; border-radius: 50%;
    border: 1.5px solid var(--rose-light);
    background: var(--paper);
    box-shadow: inset 0 0 0 2px var(--paper), inset 0 0 0 12px #fbe3df;
    color: var(--marker-red); font-weight: 700; font-size: 11px;
    display: flex; align-items: center; justify-content: center;
  }
  .sign-text { text-align: justify; }
  .sign-text strong { font-weight: 700; }

  .logo-space {
    position: absolute; left: 16px; top: 699px; width: 320px;
    font-size: 10.3px; font-weight: 700;
  }

  /* Right column */
  .side {
    position: absolute; left: 339px; top: 0; width: 231px; height: 736px;
  }
  .side-art { position: absolute; left: 0; top: 0; width: 231px; height: 466px; display: block; }
  .side-heading {
    position: absolute; left: 18px; top: 204px;
    color: #fff; font-weight: 700; font-size: 15px; line-height: 17.5px; letter-spacing: .2px;
  }
  .side-copy {
    position: absolute; left: 18px; top: 247px; width: 196px;
    color: #fff; font-weight: 700; font-size: 10.3px; line-height: 13.4px; text-align: justify;
  }
  .side-copy p + p { margin-top: 13.4px; }

  .callout {
    position: absolute; left: 0; top: 466px; width: 231px; height: 72px;
    background: var(--rose-deep);
    padding: 8px 18px 0;
    color: var(--callout-ink); font-weight: 700;
    font-size: 13.8px; line-height: 17.4px; letter-spacing: .4px; text-align: justify;
  }

  .partner {
    position: absolute; left: 18px; top: 546px; width: 200px; height: 46px;
    display: flex; align-items: center; gap: 8px;
  }
  .partner-dot { width: 44px; height: 44px; border-radius: 50%; background: var(--teal); flex: none; }
  .partner-name {
    color: var(--teal); font-weight: 700; font-size: 11.5px; line-height: 12.5px;
  }

  .learn {
    position: absolute; left: 0; top: 600px; width: 231px;
    text-align: center; color: var(--teal); font-weight: 700;
    font-size: 10.3px; line-height: 13.4px;
  }
  .links { margin-top: 3px; color: var(--link-red); font-size: 11.5px; line-height: 15.5px; }

  .network {
    position: absolute; left: 0; top: 690px; width: 231px;
    display: flex; align-items: center; justify-content: center; gap: 6px;
  }
  .network-dot { width: 14px; height: 14px; border-radius: 50%; background: var(--teal); flex: none; }
  .network-name { color: var(--link-red); font-weight: 700; font-size: 8.5px; line-height: 10px; text-align: center; width: 110px; }
</style>
</head>
<body>
  <main class="flyer">
    <section class="flyer-main">
      <header class="title-band">
        <h1 class="title-main">10 WARNING SIGNS</h1>
        <p class="title-sub">OF ABNORMAL MEMORY CHANGES<br>OR DEMENTIA</p>
      </header>

      <div class="intro">
        <p>Everyone slows down as they get older. Most people see changes in their bodies and minds. <strong>Big changes that make it hard to get through the day are not a normal part of aging.</strong></p>
        <p>Some people notice these changes in themselves. Sometimes, friends and family are the first to see changes in memory or how you act.</p>
        <p><strong>If you have one or more of these 10 warning signs, see your doctor for help.</strong></p>
      </div>

      <ol class="signs">
        <li class="sign"><span class="sign-num">1</span><p class="sign-text"><strong>Memory loss that disrupts daily life:</strong> forgetting events or important dates, repeating yourself, or relying on things to help you remember more often like lists or sticky notes.</p></li>
        <li class="sign"><span class="sign-num">2</span><p class="sign-text"><strong>New trouble planning or solving problems:</strong> having a harder time paying bills or cooking recipes you have used for years.</p></li>
        <li class="sign"><span class="sign-num">3</span><p class="sign-text"><strong>Harder to do familiar tasks at home, at work, or when you are out:</strong> having problems with driving places, using a cell phone, making a grocery list, or shopping.</p></li>
        <li class="sign"><span class="sign-num">4</span><p class="sign-text"><strong>Getting confused with time or place:</strong> forgetting where you are or how you got there, or losing track of dates or seasons.</p></li>
        <li class="sign"><span class="sign-num">5</span><p class="sign-text"><strong>Trouble with tasks that require your eyesight to connect with your thinking:</strong> having more problems with balance or telling distance, tripping over things at home, spilling or dropping things more often.</p></li>
        <li class="sign"><span class="sign-num">6</span><p class="sign-text"><strong>Getting harder to use words when talking or writing:</strong> having trouble keeping up with or joining a conversation or struggling to find a word you are looking for (saying “that thing on your wrist that tells time” instead of “watch”).</p></li>
        <li class="sign"><span class="sign-num">7</span><p class="sign-text"><strong>Losing things and not being able to retrace steps to find them:</strong> placing car keys in the washer or dryer or not being able to go back to find something you use everyday.</p></li>
        <li class="sign"><span class="sign-num">8</span><p class="sign-text"><strong>More slips in judgment or acting fast without thinking:</strong> more likely to be a scam victim, spending money you don't have, paying less attention to how you look, not washing up regularly, or forgetting to take care of your pet.</p></li>
        <li class="sign"><span class="sign-num">9</span><p class="sign-text"><strong>Pulling away from work or time with friends and family:</strong> not wanting to go to church or cultural events, loss of interest in sex, not being able to follow radio shows or keep up with what's happening in sports games.</p></li>
        <li class="sign"><span class="sign-num">10</span><p class="sign-text"><strong>Changes in mood or personality:</strong> getting angry or sad easily in every day situations, being more fearful, suspicious, or depressed for no reason.</p></li>
      </ol>

      <p class="logo-space">small space for other people to add their logo once they download.</p>
    </section>

    <aside class="side">
      <svg class="side-art" viewBox="0 0 231 466" xmlns="http://www.w3.org/2000/svg">
        <defs>
          <linearGradient id="photoTone" x1="0" y1="0" x2="1" y2="1">
            <stop offset="0" stop-color="#6f8a3e"/>
            <stop offset=".45" stop-color="#b98a63"/>
            <stop offset="1" stop-color="#e9b59c"/>
          </linearGradient>
        </defs>
        <rect x="0" y="0" width="231" height="466" fill="var(--teal)"/>
        <polygon points="0,138 177,230 231,200 231,213 177,243 0,152" fill="#ffffff"/>
        <polygon points="0,126 177,222 231,192 231,203 177,233 0,141" fill="var(--rose-light)"/>
        <polygon role="img" aria-label="Photo of a smiling elder woman outdoors in warm sunlight" points="0,0 231,0 231,192 177,222 0,126" fill="url(#photoTone)"/>
      </svg>

      <h2 class="side-heading">HEALTHY<br>MIND PROJECT</h2>
      <div class="side-copy">
        <p>American Indian and Alaska Native elders have a higher risk of dementia &amp; younger Indian and Native people report more memory problems at a younger age.</p>
        <p>Big changes in memory, thinking, and ability that make it hard to get through the day are not a normal part of aging.</p>
        <p>People with one or more of these 10 warning signs should see their doctor to find the cause.</p>
        <p>Other health problems may also cause these same symptoms and may be treated.</p>
      </div>

      <p class="callout">EARLY DIAGNOSIS GIVES YOU A CHANCE TO GET CARE AND PLAN FOR YOUR FUTURE.</p>

      <div class="partner">
        <span class="partner-dot"></span>
        <span class="partner-name">NATIVE ELDERS BRAIN<br>HEALTH CENTER</span>
      </div>

      <div class="learn">
        <p>To learn more about the warning signs<br>of dementia in American Indian and<br>Alaska Native people, visit:</p>
        <p class="links">www.ElderMindHealth.org<br>www.healthyagingnet.org/aging</p>
      </div>

      <div class="network">
        <span class="network-dot"></span>
        <span class="network-name">CIRCLE OF ELDERS AGING NETWORK</span>
      </div>
    </aside>
  </main>
</body>
</html>
```